Powerpoint design for european B2B business

We need a Powerpoint design for a newly established IT company with a B2B focus. We want to develop management information systems that help managers communicate goals into their organization and analyze their organizational activities and performance.

We defined the attached color scale, please relate your design to these colors.

The design should be simple and straight, serious and professional and leave enough space for the content ... :-)

Target Market(s)

B2B, companies larger than 200 employees

Industry/Entity Type

Business

Font styles to use
Sans Serif

Requirements
Should not have
• too playful design, clipart style

```html
<!DOCTYPE html>
<html lang="en">
<head>
<meta charset="utf-8">
<title>Quorvel — presentation template</title>
<link rel="stylesheet" href="https://fonts.googleapis.com/css2?family=Roboto:wght@300;400;700&display=swap">
<style>
  :root{
    --board:#333333;
    --navy:#1f4a72;
    --deep:#1b4a80;
    --red:#c8394f;
    --yellow:#e3dd55;
    --sage:#8bbf9a;
    --sky:#3aa0d0;
    --panel:#1f9ac8;
    --teal:#88cfc4;
    --mint:#cdebc9;
    --ink:#444444;
    --body:#333333;
    --dark:#2a2a2a;
    --white:#ffffff;
  }
  html,body{margin:0;padding:0;overflow:hidden;}
  body{width:1200px;height:1200px;background:var(--board);position:relative;font-family:"Roboto",Arial,sans-serif;}
  .slide{position:absolute;width:530px;height:298px;display:block;}
  .slide--cover{left:59px;top:132px;}
  .slide--columns{left:615px;top:132px;}
  .slide--text{left:60px;top:461px;}
  .slide--cycle{left:613px;top:461px;}
  .slide--steps{left:60px;top:782px;}
  .slide--tags{left:614px;top:782px;}

  .bg-white{fill:var(--white);}
  .fill-red{fill:var(--red);}
  .fill-yellow{fill:var(--yellow);}
  .fill-sage{fill:var(--sage);}
  .fill-navy{fill:var(--navy);}
  .fill-deep{fill:var(--deep);}
  .fill-sky{fill:var(--sky);}
  .fill-teal{fill:var(--teal);}
  .fill-dark{fill:var(--dark);}
  .fill-panel{fill:var(--panel);}
  .fill-white{fill:var(--white);}

  .stop-mint{stop-color:var(--mint);}
  .stop-teal{stop-color:var(--teal);}
  .stop-sky{stop-color:var(--sky);}
  .stop-blue{stop-color:#2a80c0;}
  .stop-panel{stop-color:var(--panel);}
  .stop-navy{stop-color:#0f5a96;}

  text{font-family:"Roboto",Arial,sans-serif;}
  .brand{font-weight:400;fill:var(--ink);}
  .tagline{font-weight:400;fill:var(--ink);font-size:15px;}
  .headline{font-weight:400;font-size:26px;fill:var(--ink);}
  .headline--light{fill:var(--white);}
  .panel-title{font-weight:300;font-size:27px;fill:var(--white);}
  .panel-copy{font-size:9px;fill:var(--white);}
  .panel-copy--bold{font-size:10px;font-weight:700;fill:var(--white);}
  .small-copy{font-size:9.3px;fill:#555;}
  .body-copy{font-size:13.5px;font-weight:700;fill:var(--body);}
  .segment-copy{font-size:6.5px;fill:var(--white);}
  .step-num{font-weight:300;fill:var(--white);}
  .tag-label{font-size:9.5px;fill:var(--white);}
  .divider{stroke:#555;stroke-width:1.2;}
  .connector{stroke:var(--ink);stroke-width:8;}
  .segment{stroke:var(--white);stroke-width:6;stroke-linejoin:round;}
</style>
</head>
<body>

<!-- Cover -->
<svg class="slide slide--cover" viewBox="0 0 630 354" role="group" aria-label="Cover slide">
  <defs>
    <linearGradient id="cover-grad" x1="0" y1="0" x2="1" y2="1">
      <stop offset="0" class="stop-mint"/>
      <stop offset="0.45" class="stop-teal"/>
      <stop offset="0.8" class="stop-sky"/>
      <stop offset="1" class="stop-blue"/>
    </linearGradient>
  </defs>
  <rect width="630" height="354" fill="url(#cover-grad)" role="img" aria-label="Faceted green-to-blue low-poly background"/>
  <rect class="bg-white" x="93" y="83" width="434" height="174"/>
  <text class="brand" x="310" y="186" font-size="64" text-anchor="middle">Quorvel</text>
  <text class="tagline" x="310" y="220" text-anchor="middle">Management Information Systems</text>
</svg>

<!-- Three columns -->
<svg class="slide slide--columns" viewBox="0 0 630 354" role="group" aria-label="Three point slide">
  <defs>
    <linearGradient id="panel-grad-a" x1="0" y1="1" x2="1" y2="0">
      <stop offset="0" class="stop-panel"/>
      <stop offset="1" class="stop-navy"/>
    </linearGradient>
    <linearGradient id="corner-grad-a" x1="0" y1="0" x2="1" y2="1">
      <stop offset="0" class="stop-mint"/>
      <stop offset="1" stop-color="#eaf6e8"/>
    </linearGradient>
  </defs>
  <rect class="bg-white" width="630" height="354"/>
  <polygon points="0,288 0,354 180,354" fill="url(#corner-grad-a)" role="img" aria-label="Faint green facet accent"/>
  <polygon points="360,0 445,0 445,60" class="fill-sky"/>
  <rect x="445" y="0" width="185" height="354" class="fill-panel"/>
  <polygon points="445,0 630,0 630,130 540,90" fill="url(#panel-grad-a)" role="img" aria-label="Faceted blue panel accent"/>
  <text class="headline" x="227" y="70" text-anchor="middle">Your Headline</text>

  <circle class="fill-red" cx="88" cy="155" r="36"/>
  <circle class="fill-yellow" cx="228" cy="155" r="36"/>
  <circle class="fill-sage" cx="368" cy="155" r="36"/>
  <line class="divider" x1="155" y1="98" x2="155" y2="305"/>
  <line class="divider" x1="297" y1="98" x2="297" y2="305"/>

  <g class="small-copy" text-anchor="middle">
    <text x="84" y="219">Lorem ipsum dolor sit amet,</text>
    <text x="84" y="230">consectetur adipiscing elit,</text>
    <text x="84" y="241">sed do eiusmod tempor</text>
    <text x="84" y="252">incididunt ut labore et</text>
    <text x="84" y="263">dolore magna aliqua. Ut</text>
    <text x="84" y="274">enim ad minim veniam.</text>
    <text x="224" y="219">Lorem ipsum dolor sit amet,</text>
    <text x="224" y="230">consectetur adipiscing elit,</text>
    <text x="224" y="241">sed do eiusmod tempor</text>
    <text x="224" y="252">incididunt ut labore et</text>
    <text x="224" y="263">dolore magna aliqua. Ut</text>
    <text x="224" y="274">enim ad minim veniam.</text>
    <text x="364" y="219">Lorem ipsum dolor sit amet,</text>
    <text x="364" y="230">consectetur adipiscing elit,</text>
    <text x="364" y="241">sed do eiusmod tempor</text>
    <text x="364" y="252">incididunt ut labore et</text>
    <text x="364" y="263">dolore magna aliqua. Ut</text>
    <text x="364" y="274">enim ad minim veniam.</text>
  </g>

  <text class="panel-title" x="460" y="158">Your Text</text>
  <text class="panel-title" x="460" y="189">Here</text>
  <g class="panel-copy">
    <text x="460" y="206">Lorem ipsum dolor sit amet,</text>
    <text x="460" y="217">consectetur adipiscing elit, sed do</text>
    <text x="460" y="228">eiusmod tempor incididunt ut labore</text>
    <text x="460" y="239">et dolore magna aliqua. Ut enim ad</text>
    <text x="460" y="250">minim veniam. Sed ut perspiciatis</text>
    <text x="460" y="261">unde omnis iste natus error sit</text>
    <text x="460" y="272">voluptatem accusantium.</text>
  </g>
  <rect class="bg-white" x="492" y="315" width="98" height="39"/>
  <text class="brand" x="541" y="341" font-size="19" text-anchor="middle">Quorvel</text>
</svg>

<!-- Text slide -->
<svg class="slide slide--text" viewBox="0 0 630 354" role="group" aria-label="Text slide">
  <defs>
    <linearGradient id="band-grad-a" x1="0" y1="0" x2="1" y2="0">
      <stop offset="0" class="stop-teal"/>
      <stop offset="0.5" class="stop-sky"/>
      <stop offset="1" class="stop-blue"/>
    </linearGradient>
  </defs>
  <rect class="bg-white" width="630" height="354"/>
  <polygon points="0,0 630,0 630,108 454,51 399,89 145,54 0,85" fill="url(#band-grad-a)" role="img" aria-label="Faceted blue header band"/>
  <text class="headline headline--light" x="314" y="42" text-anchor="middle">Your Headline</text>
  <g class="body-copy">
    <text x="74" y="147">Lorem ipsum dolor sit amet, consectetur adipiscing elit, sed do</text>
    <text x="74" y="163">eiusmod tempor incididunt ut labore et dolore magna aliqua. Ut</text>
    <text x="74" y="178">enim ad minim veniam.</text>
    <text x="74" y="220">Lorem ipsum dolor sit amet, consectetur adipiscing elit, sed do</text>
    <text x="74" y="236">eiusmod tempor incididunt ut labore et dolore magna aliqua. Ut</text>
    <text x="74" y="251">enim ad minim veniam.</text>
  </g>
  <text class="brand" x="532" y="338" font-size="19" text-anchor="middle">Quorvel</text>
</svg>

<!-- Cycle slide -->
<svg class="slide slide--cycle" viewBox="0 0 630 354" role="group" aria-label="Cycle diagram slide">
  <defs>
    <linearGradient id="panel-grad-b" x1="0" y1="1" x2="1" y2="0">
      <stop offset="0" class="stop-panel"/>
      <stop offset="1" class="stop-navy"/>
    </linearGradient>
    <linearGradient id="corner-grad-b" x1="0" y1="0" x2="1" y2="1">
      <stop offset="0" class="stop-mint"/>
      <stop offset="1" stop-color="#eaf6e8"/>
    </linearGradient>
  </defs>
  <rect class="bg-white" width="630" height="354"/>
  <polygon points="0,288 0,354 180,354" fill="url(#corner-grad-b)" role="img" aria-label="Faint green facet accent"/>
  <polygon points="360,0 445,0 445,60" class="fill-sky"/>
  <rect x="445" y="0" width="185" height="354" class="fill-panel"/>
  <polygon points="445,0 630,0 630,130 540,90" fill="url(#panel-grad-b)" role="img" aria-label="Faceted blue panel accent"/>
  <text class="headline" x="227" y="47" text-anchor="middle">Your Headline</text>

  <path class="segment fill-red" d="M142.15 108.15 A120 120 0 0 1 311.85 108.15 L255.28 164.72 A40 40 0 0 0 198.72 164.72 Z"/>
  <path class="segment fill-deep" d="M311.85 108.15 A120 120 0 0 1 311.85 277.85 L255.28 221.28 A40 40 0 0 0 255.28 164.72 Z"/>
  <path class="segment fill-sky" d="M311.85 277.85 A120 120 0 0 1 142.15 277.85 L198.72 221.28 A40 40 0 0 0 255.28 221.28 Z"/>
  <path class="segment fill-yellow" d="M142.15 277.85 A120 120 0 0 1 142.15 108.15 L198.72 164.72 A40 40 0 0 0 198.72 221.28 Z"/>

  <path class="fill-white" d="M227 82 a9 9 0 0 1 9 9 c0 7 -9 16 -9 16 s-9 -9 -9 -16 a9 9 0 0 1 9 -9 z"/>
  <circle class="fill-red" cx="227" cy="91" r="3.5"/>
  <path class="fill-white" d="M128 180 h30 a6 6 0 0 0 0 -12 a9 9 0 0 0 -17 -3 a7 7 0 0 0 -13 8 a4 4 0 0 0 0 7 z"/>
  <g class="fill-white">
    <rect x="288" y="176" width="4" height="9"/>
    <rect x="294" y="172" width="4" height="13"/>
    <rect x="300" y="168" width="4" height="17"/>
    <rect x="306" y="164" width="4" height="21"/>
  </g>
  <path d="M287 170 L298 162 L312 156" stroke="#ffffff" stroke-width="1.5" fill="none"/>
  <g class="fill-white">
    <circle cx="227" cy="288" r="9"/>
    <rect x="224.5" y="275" width="5" height="26"/>
    <rect x="214" y="285.5" width="26" height="5"/>
    <rect x="224.5" y="275" width="5" height="26" transform="rotate(45 227 288)"/>
    <rect x="224.5" y="275" width="5" height="26" transform="rotate(-45 227 288)"/>
  </g>
  <circle class="fill-sky" cx="227" cy="288" r="4"/>

  <g class="segment-copy" text-anchor="middle">
    <text x="227" y="124">Lorem ipsum dolor sit amet,</text>
    <text x="227" y="132">consectetur adipiscing elit.</text>
    <text x="150" y="195">Lorem ipsum</text>
    <text x="150" y="203">dolor sit amet,</text>
    <text x="150" y="211">consectetur</text>
    <text x="150" y="219">adipiscing elit.</text>
    <text x="305" y="195">Lorem ipsum</text>
    <text x="305" y="203">dolor sit amet,</text>
    <text x="305" y="211">consectetur</text>
    <text x="305" y="219">adipiscing elit.</text>
    <text x="227" y="251">Lorem ipsum dolor sit amet,</text>
    <text x="227" y="259">consectetur adipiscing elit.</text>
  </g>

  <text class="panel-title" x="460" y="126">Your Text</text>
  <text class="panel-title" x="460" y="157">Here</text>
  <g class="panel-copy--bold">
    <text x="460" y="186">Lorem ipsum dolor sit amet,</text>
    <text x="460" y="198">consectetur adipiscing elit,</text>
    <text x="460" y="210">sed do eiusmod tempor</text>
    <text x="460" y="222">incididunt ut labore et dolore</text>
    <text x="460" y="234">magna aliqua. Ut enim ad</text>
    <text x="460" y="246">minim veniam. Sed ut</text>
    <text x="460" y="258">perspiciatis unde omnis iste</text>
    <text x="460" y="270">natus error sit voluptatem</text>
    <text x="460" y="282">accusantium.</text>
  </g>
  <rect class="bg-white" x="499" y="314" width="99" height="40"/>
  <text class="brand" x="548" y="341" font-size="19" text-anchor="middle">Quorvel</text>
</svg>

<!-- Steps slide -->
<svg class="slide slide--steps" viewBox="0 0 630 354" role="group" aria-label="Process steps slide">
  <defs>
    <linearGradient id="band-grad-b" x1="0" y1="0" x2="1" y2="0">
      <stop offset="0" class="stop-teal"/>
      <stop offset="0.5" class="stop-sky"/>
      <stop offset="1" class="stop-blue"/>
    </linearGradient>
  </defs>
  <rect class="bg-white" width="630" height="354"/>
  <polygon points="0,0 630,0 630,108 454,51 399,89 145,54 0,85" fill="url(#band-grad-b)" role="img" aria-label="Faceted blue header band"/>
  <text class="headline headline--light" x="314" y="42" text-anchor="middle">Your Headline</text>

  <line class="connector" x1="164" y1="186" x2="202" y2="214"/>
  <line class="connector" x1="313" y1="214" x2="353" y2="184"/>
  <line class="connector" x1="431" y1="186" x2="475" y2="216"/>

  <circle class="fill-yellow" cx="129" cy="163" r="30"/>
  <circle class="fill-red" cx="257" cy="253" r="56"/>
  <circle class="fill-deep" cx="392" cy="158" r="37"/>
  <circle class="fill-teal" cx="516" cy="246" r="39"/>
  <text class="step-num" x="129" y="172" font-size="26" text-anchor="middle">01</text>
  <text class="step-num" x="257" y="269" font-size="46" text-anchor="middle">02</text>
  <text class="step-num" x="392" y="170" font-size="33" text-anchor="middle">03</text>
  <text class="step-num" x="516" y="258" font-size="35" text-anchor="middle">04</text>

  <g class="small-copy" text-anchor="middle">
    <text x="257" y="141">Lorem ipsum dolor sit amet,</text>
    <text x="257" y="152">consectetur adipiscing elit,</text>
    <text x="257" y="163">sed do eiusmod tempor</text>
    <text x="100" y="222">Lorem ipsum dolor sit amet,</text>
    <text x="100" y="233">consectetur adipiscing elit, sed</text>
    <text x="100" y="244">do eiusmod tempor</text>
    <text x="397" y="233">Lorem ipsum dolor sit amet,</text>
    <text x="397" y="244">consectetur adipiscing elit, sed</text>
    <text x="397" y="255">do eiusmod tempor</text>
    <text x="522" y="162">Lorem ipsum dolor sit amet,</text>
    <text x="522" y="173">consectetur adipiscing elit,</text>
    <text x="522" y="184">sed do eiusmod tempor</text>
  </g>
  <text class="brand" x="534" y="340" font-size="19" text-anchor="middle">Quorvel</text>
</svg>

<!-- Tags slide -->
<svg class="slide slide--tags" viewBox="0 0 630 354" role="group" aria-label="Six topics slide">
  <defs>
    <linearGradient id="band-grad-c" x1="0" y1="0" x2="1" y2="0">
      <stop offset="0" class="stop-teal"/>
      <stop offset="0.5" class="stop-sky"/>
      <stop offset="1" class="stop-blue"/>
    </linearGradient>
  </defs>
  <rect class="bg-white" width="630" height="354"/>
  <polygon points="0,0 630,0 630,106 470,52 400,90 160,54 0,82" fill="url(#band-grad-c)" role="img" aria-label="Faceted blue header band"/>
  <text class="headline headline--light" x="314" y="42" text-anchor="middle">Your Headline</text>

  <g class="fill-red">
    <rect x="76" y="114" width="112" height="17"/>
    <polygon points="192,131 201,114 218,114 209,131"/>
  </g>
  <g class="fill-yellow">
    <rect x="244" y="114" width="112" height="17"/>
    <polygon points="360,131 369,114 386,114 377,131"/>
  </g>
  <g class="fill-deep">
    <rect x="421" y="114" width="112" height="17"/>
    <polygon points="537,131 546,114 563,114 554,131"/>
  </g>
  <g class="fill-sky">
    <rect x="76" y="227" width="112" height="17"/>
    <polygon points="192,244 201,227 218,227 209,244"/>
  </g>
  <g class="fill-sage">
    <rect x="244" y="227" width="112" height="17"/>
    <polygon points="360,244 369,227 386,227 377,244"/>
  </g>
  <g class="fill-dark">
    <rect x="421" y="227" width="112" height="17"/>
    <polygon points="537,244 546,227 563,227 554,244"/>
  </g>

  <g class="tag-label">
    <text x="102" y="126">LOREM IPSUM</text>
    <text x="270" y="126">LOREM IPSUM</text>
    <text x="447" y="126">LOREM IPSUM</text>
    <text x="102" y="239">LOREM IPSUM</text>
    <text x="270" y="239">LOREM IPSUM</text>
    <text x="447" y="239">LOREM IPSUM</text>
  </g>

  <g class="small-copy">
    <text x="77" y="154">Lorem ipsum dolor sit amet</text>
    <text x="77" y="165">consectetur adipiscing elit,</text>
    <text x="77" y="176">sed do eiusmod tempor</text>
    <text x="245" y="154">Lorem ipsum dolor sit amet</text>
    <text x="245" y="165">consectetur adipiscing elit,</text>
    <text x="245" y="176">sed do eiusmod tempor</text>
    <text x="422" y="154">Lorem ipsum dolor sit amet</text>
    <text x="422" y="165">consectetur adipiscing elit,</text>
    <text x="422" y="176">sed do eiusmod tempor</text>
    <text x="77" y="267">Lorem ipsum dolor sit amet</text>
    <text x="77" y="278">consectetur adipiscing elit,</text>
    <text x="77" y="289">sed do eiusmod tempor</text>
    <text x="245" y="267">Lorem ipsum dolor sit amet</text>
    <text x="245" y="278">consectetur adipiscing elit,</text>
    <text x="245" y="289">sed do eiusmod tempor</text>
    <text x="422" y="267">Lorem ipsum dolor sit amet</text>
    <text x="422" y="278">consectetur adipiscing elit,</text>
    <text x="422" y="289">sed do eiusmod tempor</text>
  </g>
  <text class="brand" x="536" y="340" font-size="19" text-anchor="middle">Quorvel</text>
</svg>

</body>
</html>
```